Our Velvetline

I am developing a web site which sells preowned high end designer handbags and accessories. Some of the brands include: Duvore, Marcel Ostrand & Velka, to name a few. I am after a luxurious and high end feel.

Some brands I like that express this feel include: Corvin, Velka, thecloset-kip.com, pursetradeorloan.com

I am after a logo, business card, letterhead, with compliments, address label and envelope designs.
The business name is Our velvetline, and the website will be www.ourvelvetline.com.au. I have thoughts of using OVL as a logo or OUR velvetline.com.au

I don't want a large logo, it needs to blend in with the name in some way - or may not need an image at all, if the style of the font speaks to the brand.

Thank-you

Reason: I would like to give designers plenty of time to be able to submit a design.

Target Market(s)

Women, aged 25-60 who are into fashion

Industry/Entity Type

Business

Requirements
Must have
• High End
Luxurious

```html
<!DOCTYPE html>
<html lang="en">
<head>
<meta charset="utf-8">
<title>Our Velvetline – Stationery</title>
<link href="https://fonts.googleapis.com/css2?family=Questrial&display=swap" rel="stylesheet">
<style>
  :root {
    --page: #ffffff;
    --board: #939598;
    --wine: #8b1c1c;
    --wine-light: #ad2428;
    --plum: #26143f;
    --plum-light: #3c2760;
    --gold: #b08a4e;
    --ink: #111111;
    --paper: #ffffff;
    --shadow: 4px 5px 7px rgba(0,0,0,0.35);
  }
  * { margin: 0; padding: 0; box-sizing: border-box; }
  html, body { width: 1200px; height: 900px; overflow: hidden; background: var(--page); }
  body { font-family: "Questrial", Arial, sans-serif; position: relative; }

  .board { position: absolute; left: 34px; top: 34px; width: 1132px; height: 832px; background: var(--board); }
  .board-title { position: absolute; left: 83px; top: 117px; color: #fff; font-size: 11px; letter-spacing: 0.2px; display: flex; align-items: center; gap: 4px; }
  .board-title .num { display: inline-block; background: #fff; color: var(--board); font-size: 9px; width: 11px; height: 11px; line-height: 11px; text-align: center; border-radius: 1px; }

  .wordmark { font-family: "Questrial", Arial, sans-serif; color: var(--gold); letter-spacing: 1px; white-space: nowrap; }

  .card { position: absolute; width: 213px; height: 133px; border-radius: 4px; box-shadow: var(--shadow); overflow: hidden; }
  .card-front { left: 115px; top: 286px; background: var(--wine); display: flex; align-items: center; justify-content: center; }
  .card-front .wordmark { font-size: 17px; }
  .card-back { display: flex; align-items: center; justify-content: center; }
  .card-back.wine { left: 351px; top: 170px; background: linear-gradient(120deg, var(--wine) 0%, var(--wine-light) 55%, var(--wine) 100%); }
  .card-back.plum { left: 351px; top: 337px; background: linear-gradient(120deg, var(--plum) 0%, var(--plum-light) 55%, var(--plum) 100%); }
  .card-back .url { color: #fff; font-size: 7px; }

  .envelope { position: absolute; left: 126px; top: 557px; width: 490px; height: 222px; background: var(--paper); box-shadow: var(--shadow); }
  .envelope-band { position: absolute; left: 0; top: 0; width: 52px; height: 100%; background: linear-gradient(170deg, var(--wine-light) 0%, var(--wine) 45%); }
  .envelope-band .url { position: absolute; left: 21px; top: 72px; color: #fff; font-size: 7px; writing-mode: vertical-rl; transform: rotate(180deg); }

  .contact { position: absolute; font-size: 6.5px; color: var(--ink); line-height: 9px; text-align: right; }
  .contact p + p { margin-top: 8px; }
  .contact .company { letter-spacing: 0.3px; }

  .envelope .wordmark { position: absolute; right: 32px; top: 40px; font-size: 15px; }
  .envelope .contact { right: 32px; top: 112px; }

  .letterhead { position: absolute; left: 669px; top: 134px; width: 435px; height: 659px; background: var(--paper); box-shadow: var(--shadow); border-radius: 3px; overflow: hidden; }
  .letterhead .wordmark { position: absolute; right: 22px; top: 42px; font-size: 15px; }
  .letterhead .contact { right: 32px; top: 100px; }
  .letterhead-footer { position: absolute; left: 0; bottom: 0; width: 100%; height: 52px; background: linear-gradient(90deg, var(--wine-light) 0%, var(--wine) 40%); }
  .letterhead-footer .url { position: absolute; right: 30px; top: 23px; color: #fff; font-size: 7px; }
</style>
</head>
<body>
  <div class="board"></div>
  <div class="board-title">Stationary design Ourvelvetline <span class="num">2</span></div>

  <div class="card card-back wine" role="img" aria-label="Business card back with large faint brand monogram">
    <span class="url">ourvelvetline.com.au</span>
  </div>
  <div class="card card-front">
    <span class="wordmark">OUR VELVETLINE</span>
  </div>
  <div class="card card-back plum" role="img" aria-label="Business card back in plum with large faint brand monogram">
    <span class="url">ourvelvetline.com.au</span>
  </div>

  <div class="envelope">
    <div class="envelope-band" role="img" aria-label="Wine band with faint brand monogram">
      <span class="url">ourvelvetline.com.au</span>
    </div>
    <span class="wordmark">OUR VELVETLINE</span>
    <div class="contact">
      <p class="company">OUR VELVETLINE</p>
      <p>T. (02) 5550 1928<br>E. hello@ourvelvetline.com</p>
      <p>PO BOX 4410<br>88 Sample Lane NY</p>
    </div>
  </div>

  <div class="letterhead">
    <span class="wordmark">OUR VELVETLINE</span>
    <div class="contact">
      <p class="company">OUR VELVETLINE</p>
      <p>tel (02) 5550 1928<br>e-mail hello@ourvelvetline.com</p>
      <p>PO BOX 4410<br>88 Sample Lane NY</p>
    </div>
    <div class="letterhead-footer" role="img" aria-label="Wine footer band with faint brand monogram">
      <span class="url">ourvelvetline.com.au</span>
    </div>
  </div>
</body>
</html>
```